Want to learn how to safely prescribe Testosterone, bio-identical hormones and become an expert? I can teach you in 1 weekend!
I have developed and designed Prime Vital Horizon: the worlds first complete Anti-Aging Medical Platform with a "one-stop-learn-workshop tier" where a medical provider can attend my 3-Day Modern Frontier Bright Years Renewal Seminar.
During the 3 days the medical provider will become an expert in:
1. Identifying, stratifying and qualifying the appropriate patient for the anti-age hormonal protocol
2. Prescribing Testosterone, Estrogen, Progesterone, Dhea, HcG HgH, both men and women, when appropriate, using my unique and proprietary medically supervised hormone optimization protocol (the protocol as long as my hormone book will be made available to all course attendants)
3. Understanding nutraceuticals and recommending them when appropriate. NovaPeakFORM, the most perfectly developed multi-vitamin, mineral and anti-oxidant pack on the market will be made available for all course attendants to try for free
4. Prescribing a complete and powerful medically optimized weight loss program backed by my proprietary medically supervised protocol and published book (both the protocol and book are available free to all course attendants)
5. Understanding the exercise challenge and understanding what kind of exercise should be prescribed, to whom and in what form. (an extensive proprietary video exercise video library will be available for all course attendants)
6. Upon completion of the workshop each attendee will be proficient enough that upon return to his/her office on Monday, he/she will be able to greatly increase his/her revenue with the knowledge learned.
7. Upon request, the attendee can remain on as affiliate physician of Prime Vital Horizon and learn directly from Dr Verhoeven who will help manage each affiliate physician's n.patient until the affiliate physician is confident enough on his/her own

The course will be held on a Saturday and Sunday in Hollywood Florida at the Coralview Lodge in sunny South Florida

The Course will begin at 930am and end at 3pm each day allowing ample time for sun and fun

I want the email to be STUNNING , to catch the eye of the doctor as this is who I will be sending it to, I want the doctor who opens this email to NOT trash it, to be hypnotized by it, to be intrigued by it, to go ahead and book this course!!!

I will include the logos of Prime Vital Horizon, NovaPeakForm and my weight loss book

Please keep in mind this email MUST be stunning!!! It will be emailed blindly solely to physicians who are notoriously busy and usually trash unknown emails.

I also need to be able to edit the template

Target Market(s)

Doctors

Industry/Entity Type

Medical

Font styles to use
Serif
Sans Serif
Decorative
Script

Colors

Designer to choose colors to be used in the design.

Requirements
Must have
• Stunning colors
• Catchy fonts
• Cool graphics
Nice to have
• an email that is not easily deleted!
• an email that hypnotizes the doctor
• an email that tells the doctor "this is the course I must take!!"
• and email that tells the doctor "if I dont take this course I am a fool"
Should not have
• Negative connotations

```html
<!DOCTYPE html>
<html lang="en">
<head>
<meta charset="utf-8">
<title>Prime Vital Horizon – Hormone Workshop</title>
<link rel="stylesheet" href="https://fonts.googleapis.com/css2?family=Montserrat:wght@400;500;600;700&family=Open+Sans:wght@400;600;700&display=swap">
<style>
:root{
  --backdrop:#cfcfcf;
  --paper:#f6f6f6;
  --white:#ffffff;
  --red:#ee1c25;
  --red-soft:#f04a50;
  --red-dark:#c8161d;
  --ink:#2b2b2b;
  --grey:#555555;
  --grey-light:#8a8a8a;
  --line:#c9c9c9;
}
*{box-sizing:border-box;margin:0;padding:0}
html,body{width:1200px;height:2439px;overflow:hidden}
body{background:var(--backdrop);font-family:"Open Sans",Arial,sans-serif;color:var(--grey);position:relative}
.email{position:absolute;left:226px;top:122px;width:751px;height:2130px;background:var(--paper);border-top:5px solid var(--red);box-shadow:0 24px 30px -14px rgba(0,0,0,.35)}
.abs{position:absolute}

.brand{left:34px;top:52px}
.brand-name{font-family:"Montserrat",sans-serif;font-weight:500;font-size:31px;color:var(--ink);letter-spacing:-.3px}

.social{left:603px;top:54px;display:flex;gap:7px}
.social span{width:33px;height:33px;display:block}
.social span:nth-child(1){background:#3b5998}
.social span:nth-child(2){background:#1da1f2}
.social span:nth-child(3){background:var(--red)}

.hero{left:29px;top:158px;width:690px;height:237px;background:linear-gradient(90deg,var(--red-soft),var(--red) 60%)}
.hero-icon{position:absolute;left:55px;top:70px}
.hero-text{position:absolute;left:199px;top:64px;width:460px}
.hero-title{font-family:"Montserrat",sans-serif;font-weight:700;font-size:22.5px;line-height:30px;color:var(--white)}
.hero-badge{margin-top:6px;width:426px;height:52px;background:var(--red-dark);color:var(--white);font-family:"Montserrat",sans-serif;font-weight:700;font-size:22px;line-height:52px;padding-left:20px}

.portrait{left:34px;top:426px;width:156px;height:156px;border-radius:50%;border:5px solid #e8e2d8;background:radial-gradient(circle at 50% 40%,#d9b79a,#a08872 60%,#e6ddd3)}
.intro{left:208px;top:436px;width:524px;font-size:16.5px;line-height:26px;color:var(--grey)}
.intro strong{font-family:"Montserrat",sans-serif;font-weight:700;font-size:21px;color:var(--red)}

.cta{left:172px;top:606px;width:405px;height:59px;background:var(--red);color:var(--white);font-family:"Montserrat",sans-serif;font-weight:700;font-size:17.5px;display:flex;align-items:center;justify-content:center;gap:8px;text-decoration:none}

.team{left:42px;top:683px;width:683px;height:276px;background:linear-gradient(180deg,#f6f6f6 0%,#e4e8ec 30%,#f2f4f6 70%,#dfe3e8 100%)}
.schedule{left:94px;top:821px;width:563px;height:171px;background:rgba(255,255,255,.96);border:1px solid #d8d8d8}
.schedule-time{position:absolute;left:0;top:20px;width:400px;text-align:center;font-family:"Montserrat",sans-serif;font-weight:700;font-size:30px;color:var(--red)}
.schedule-note{position:absolute;left:30px;top:78px;width:350px;text-align:center;font-family:"Montserrat",sans-serif;font-weight:600;font-size:16px;line-height:22px;color:var(--grey)}
.schedule-flag{position:absolute;right:0;top:0;width:168px;height:100%;background:var(--red-soft);clip-path:polygon(38% 0,100% 0,100% 100%,0 100%)}
.schedule-flag svg{position:absolute;left:68px;top:52px}

.outcomes-title{left:0;top:1041px;width:751px;text-align:center;font-family:"Montserrat",sans-serif;font-weight:500;font-size:31px;line-height:38px;color:var(--red)}
.timeline{left:90px;top:1142px;width:2px;height:636px;background:var(--grey)}
.step{position:absolute;left:130px;width:585px;font-size:16.5px;line-height:24.5px;color:var(--grey)}
.step-num{position:absolute;left:-53px;top:-1px;width:28px;height:28px;border:2px solid var(--grey);border-radius:50%;background:var(--paper);font-size:13px;line-height:24px;text-align:center;color:var(--ink)}

.footer{left:31px;top:1891px;width:684px;height:203px;background:var(--white);box-shadow:0 2px 8px rgba(0,0,0,.06)}
.footer-badge{position:absolute;left:320px;top:-22px;width:44px;height:44px;border-radius:50%;background:var(--white);display:flex;align-items:center;justify-content:center}
.contact{position:absolute;left:31px;top:32px;font-size:16px;line-height:29px;color:var(--grey)}
.contact .address{font-weight:600;line-height:25px;margin-top:4px;color:var(--ink)}
.footer-divider{position:absolute;left:342px;top:40px;width:1px;height:125px;background:var(--line)}
.footer-brand{position:absolute;left:420px;top:62px}
.footer-social{display:flex;gap:7px}
.footer-social span{width:30px;height:30px;border:2px solid var(--grey-light);border-radius:50%;display:block}
.footer-name{font-family:"Montserrat",sans-serif;font-weight:500;font-size:18px;color:var(--grey-light);margin-top:10px}
.copyright{font-family:"Montserrat",sans-serif;font-weight:700;font-size:16.5px;color:var(--red);margin-top:12px;margin-left:-3px}
</style>
</head>
<body>
<main class="email">
  <header class="abs brand">
    <div class="brand-name">Prime Vital Horizon</div>
  </header>
  <nav class="abs social" aria-label="Social links"><span></span><span></span><span></span></nav>

  <section class="abs hero">
    <svg class="hero-icon" width="96" height="124" viewBox="0 0 96 124" fill="none" stroke="#fff" stroke-width="6" stroke-linejoin="round">
      <rect x="20" y="4" width="56" height="18" rx="3"/>
      <path d="M26 22v10L8 46v70a4 4 0 0 0 4 4h72a4 4 0 0 0 4-4V46L70 32V22"/>
      <line x1="8" y1="54" x2="88" y2="54"/>
      <line x1="8" y1="104" x2="88" y2="104"/>
      <path d="M48 66v28M34 80h28" stroke-linecap="round"/>
    </svg>
    <div class="hero-text">
      <h1 class="hero-title">Want to learn how to safely prescribe Testosterone, bio-identical hormones and become an expert?</h1>
      <div class="hero-badge">I can teach you in 1 weekend!</div>
    </div>
  </section>

  <div class="abs portrait" role="img" aria-label="Portrait photo of the physician presenting the seminar"></div>
  <p class="abs intro">I have developed and designed Prime Vital Horizon: the worlds first complete Anti-Aging Medical Platform with a<br><strong>"one-stop-learn-workshop tier"</strong> where a medical provider can attend my 3-Day Modern Frontier Bright Years Renewal Seminar.</p>

  <a class="abs cta" href="#">
    <svg width="18" height="26" viewBox="0 0 18 26" fill="none" stroke="#fff" stroke-width="2"><rect x="3" y="1" width="12" height="5"/><rect x="1" y="6" width="16" height="19"/><line x1="1" y1="11" x2="17" y2="11"/><line x1="1" y1="20" x2="17" y2="20"/></svg>
    Come My Website to Know More
    <svg width="14" height="14" viewBox="0 0 14 14" fill="none" stroke="#fff" stroke-width="2"><path d="M2 2l5 5-5 5M7 2l5 5-5 5"/></svg>
  </a>

  <div class="abs team" role="img" aria-label="Photo of a group of doctors and nurses in white coats"></div>
  <div class="abs schedule">
    <div class="schedule-time">9:30am a- 3:00pm</div>
    <p class="schedule-note">The course will be held on a Saturday and Sunday in Hollywood Florida at the Coralview Lodge in sunny South Florida</p>
    <div class="schedule-flag">
      <svg width="70" height="70" viewBox="0 0 70 70" fill="none" stroke="#fff" stroke-width="5" stroke-linecap="round"><circle cx="35" cy="35" r="31"/><path d="M35 16v20l12 9"/></svg>
    </div>
  </div>

  <h2 class="abs outcomes-title">During the 3 days the medical provider<br>will become an expert in:</h2>
  <div class="abs timeline"></div>

  <p class="step" style="top:1132px"><span class="step-num">1</span>&nbsp;Identifying, stratifying and qualifying the appropriate patient for the anti-age hormonal protocol</p>
  <p class="step" style="top:1192px"><span class="step-num">2</span>Prescribing Testosterone, Estrogen, Progesterone, Dhea, HcG HgH, both men and women, when appropriate, using my unique and proprietary medically supervised hormone optimization protocol (the protocol as long as my hormone book will be made available to all course attendants)</p>
  <p class="step" style="top:1330px"><span class="step-num">3</span>&nbsp;Understanding nutraceuticals and recommending them when appropriate. NovaPeakFORM, the most perfectly developed multi-vitamin, mineral and anti-oxidant pack on the market will be made available for all course attendants to try for free</p>
  <p class="step" style="top:1445px"><span class="step-num">4</span>Prescribing a complete and powerful medically optimized weight loss program backed by my proprietary medically supervised protocol and published book (both the protocol and book are available free to all course attendants)</p>
  <p class="step" style="top:1559px"><span class="step-num">5</span>Understanding the exercise challenge and understanding what kind of exercise should be prescribed, to whom and in what form. (an extensive proprietary video exercise video library will be available for all course attendants)</p>
  <p class="step" style="top:1673px"><span class="step-num">6</span>Upon completion of the workshop each attendee will be proficient enough that upon return to his/her office on Monday, he/she will be able to greatly increase his/her revenue with the knowledge learned.</p>
  <p class="step" style="top:1763px"><span class="step-num">7</span>Upon request, the attendee can remain on as affiliate physician of Prime Vital Horizon and learn directly from Dr Verhoeven who will help manage each affiliate physician's n.patient until the affiliate physician is confident enough on his/her own</p>

  <footer class="abs footer">
    <div class="footer-badge">
      <svg width="18" height="26" viewBox="0 0 18 26" fill="none" stroke="#666" stroke-width="2"><rect x="3" y="1" width="12" height="5"/><rect x="1" y="6" width="16" height="19"/><line x1="1" y1="11" x2="17" y2="11"/><line x1="1" y1="20" x2="17" y2="20"/></svg>
    </div>
    <div class="contact">
      <div>954-555-0142</div>
      <div>954-555-0178</div>
      <div>support@primevitalhorizon.com</div>
      <div class="address">2250 Seabreeze Parkway,<br>Harbor Point FL 33010</div>
    </div>
    <div class="footer-divider"></div>
    <div class="footer-brand">
      <div class="footer-social"><span></span><span></span><span></span></div>
      <div class="footer-name">Prime Vital Horizon</div>
      <div class="copyright">© 2017 Prime Vital Horizon.</div>
    </div>
  </footer>
</main>
</body>
</html>
```